Corporate Personal Training Business needs a flyer for High Scale apartment complex contract

We are looking at getting a flyer for a high scale apartment complex that will explain the prices and services on the back page and offer a complimentary personal training session on the front page as well as a welcome and so on. I will attach plenty of information and also a copy of a basic flyer that does not look very good but will give you an understanding of what I am looking at doing.

Attached I will include all required information as well as pictures I wish to be used in the flyer also and any other information I can think of adding.

Logo design is already done but I am open to suggestion for new logos if you would like to make that part of the project.

The opening day for this project is on Sunday the 14th of July so I do not have a massive amount of time but more then enough to get the project done.

All required pictures can be accessed via the files I have uploaded.

Please note that 72 Marlow logo needs to be the same as the file I have attached.
Updates

PDF Format of the flyer has been uploaded here you can find logos, photos and information that is required.

All info on the flyer needs to be included just needs to look much more professional. Thankyou

Target Market(s)

Upmarket business people for the most part might have a few young people but generally 35+

Industry/Entity Type

Apartment

Requirements
Must have
• From page one you will see various pictures displaying the types of training I can provide. Kettlebells weights kickboxing etc. These pictures are required unless you feel they will be placed in written form somewhere to make it look better. I liked the idea of making that visual but it is up to you.

The flyer must be 1 page front and back with the front being very attractive to the eye and outlining the complimentary PT session. The info displayed on the front page can be shortened down if necessary as long as the basic idea is projected across and people are aware that the services provided have a wide variety and are fun.

I want the photo of the trainer included as well as the logo above info is also required such as ABN number business name obviously and so on.

Also There needs to be mention that the Owners Corporation will be covering cost of the induction until Jan 2014

Should not have
• A different font with 72 Marlow the attached image on the flyer is what needs to be used as its the 72 marlow logo

```html
<!DOCTYPE html>
<html lang="en">
<head>
<meta charset="utf-8">
<title>72 Marlow – Fitness Training</title>
<link rel="stylesheet" href="https://fonts.googleapis.com/css2?family=Arimo:wght@400;700&family=Roboto:wght@300;700&family=Roboto+Condensed:wght@400;700&family=Tinos:wght@400&display=swap">
<style>
  :root {
    --ink: #111111;
    --paper: #ffffff;
    --blue: #2b8fd4;
    --blue-deep: #1f7cc0;
    --orange: #f7941d;
    --teal: #1a8f7e;
    --body-text: #3a3a3a;
    --photo-dark: #2a2a2a;
  }
  * { box-sizing: border-box; margin: 0; padding: 0; }
  html, body { width: 927px; height: 1200px; overflow: hidden; background: var(--paper); }
  .flyer { position: relative; width: 927px; height: 1200px; background: var(--paper); font-family: "Arimo", Arial, sans-serif; }

  .hero { position: absolute; left: 27px; top: 30px; width: 873px; height: 465px; background: var(--ink); border-top-left-radius: 24px; overflow: hidden; }
  .hero-photo { position: absolute; left: 120px; top: 0; width: 400px; height: 465px;
    background: radial-gradient(ellipse at 50% 45%, #8a8a8a 0%, #4a4a4a 45%, var(--ink) 80%); }
  .venue-name { position: absolute; left: 40px; top: 48px; color: var(--paper); font-family: "Arimo", Arial, sans-serif; font-weight: 700; font-size: 30px; letter-spacing: 2px; }

  .headline { position: absolute; left: 0; top: 0; color: var(--paper); font-family: "Roboto", Arial, sans-serif; }
  .headline-top { position: absolute; left: 563px; top: 195px; font-weight: 700; font-size: 74px; line-height: 1; }
  .headline-bottom { position: absolute; left: 483px; top: 272px; font-weight: 300; font-size: 98px; line-height: 1; letter-spacing: -1px; }

  .brand-card { position: absolute; right: 0; top: 0; width: 385px; height: 144px; background: var(--paper); border-bottom-left-radius: 34px; text-align: center; padding-top: 48px; padding-right: 40px; }
  .brand-name { font-family: "Tinos", serif; font-size: 22px; color: var(--teal); }
  .brand-tagline, .brand-abn { font-family: "Tinos", serif; font-size: 15px; color: var(--ink); line-height: 1.35; }
  .brand-mark { position: absolute; right: 22px; top: 30px; width: 40px; height: 40px; border: 2px solid var(--teal); }

  .intro { position: absolute; left: 52px; top: 524px; width: 474px; font-size: 15px; line-height: 1.38; color: var(--body-text); }
  .intro p + p { margin-top: 14px; }

  .trainer-card { position: absolute; left: 548px; top: 433px; width: 328px; height: 410px; background: var(--blue); padding: 24px 18px 0 28px; color: var(--paper); }
  .trainer-tab { position: absolute; left: 6px; top: 24px; width: 282px; height: 37px; background: var(--orange); font-family: "Roboto", Arial, sans-serif; font-weight: 300; font-size: 27px; line-height: 37px; padding-left: 14px; }
  .trainer-name { position: absolute; left: 28px; top: 76px; font-family: "Roboto Condensed", Arial, sans-serif; font-weight: 700; font-size: 34px; }
  .credentials { position: absolute; left: 26px; top: 130px; right: 16px; list-style: none; }
  .credentials li { position: relative; padding-left: 27px; font-family: "Roboto Condensed", Arial, sans-serif; font-size: 16px; line-height: 1.25; margin-bottom: 11px; }
  .credentials svg { position: absolute; left: 0; top: 1px; width: 18px; height: 18px; }

  .gallery { position: absolute; top: 863px; height: 141px; }
  .gallery-kettlebell { left: 55px; width: 263px; background: linear-gradient(135deg, #c98a6a, #7a3b2a 60%, #2e2e2e); }
  .gallery-boxing { left: 333px; width: 261px; background: linear-gradient(135deg, #e6e2de, #c9553f 55%, #8c2a20); }
  .gallery-weights { left: 606px; width: 267px; background: linear-gradient(135deg, #f0f4f8, #3a6fb0 55%, #2b2b2b); }

  .offer { position: absolute; left: 40px; top: 1014px; width: 847px; text-align: center; color: var(--orange); font-weight: 700; font-size: 17.5px; line-height: 1.3; }

  .contact-band { position: absolute; left: 55px; top: 1070px; width: 818px; height: 93px; background: var(--blue); color: var(--paper); }
  .contact-label { position: absolute; left: 14px; top: 24px; width: 180px; text-align: center; font-weight: 700; font-size: 15.5px; line-height: 1.45; }
  .contact-divider { position: absolute; top: 12px; width: 1px; height: 69px; background: rgba(255,255,255,0.8); }
  .contact-person { position: absolute; left: 215px; top: 18px; font-family: "Roboto Condensed", Arial, sans-serif; font-size: 27px; line-height: 1.05; letter-spacing: 1px; }
  .contact-phone { position: absolute; left: 374px; top: 10px; font-family: "Roboto Condensed", Arial, sans-serif; font-weight: 700; font-size: 39px; }
  .contact-web { position: absolute; left: 376px; top: 60px; font-family: "Roboto Condensed", Arial, sans-serif; font-weight: 700; font-size: 18px; }
</style>
</head>
<body>
<main class="flyer">
  <section class="hero">
    <div class="hero-photo" role="img" aria-label="Black and white portrait of a shirtless personal trainer"></div>
    <div class="venue-name">72 MARLOW</div>
    <h1 class="headline">
      <span class="headline-top">Fitness</span>
      <span class="headline-bottom">Training</span>
    </h1>
  </section>

  <header class="brand-card">
    <div class="brand-name">Steady Pulse Wellness</div>
    <div class="brand-tagline">Corporate Personal Training</div>
    <div class="brand-abn">ABN: 63 518 227 409</div>
    <span class="brand-mark" aria-hidden="true"></span>
  </header>

  <section class="intro">
    <p>72 Marlow and Steady Pulse Wellness have joined together to provide you with the convenience of one on one personal training within the privacy and comfort of your apartment complex in the Health &amp; Wellbeing Retreat .</p>
    <p>Whether your goal is to lose weight, tone up, increase fitness or to feel great for Summer we have a fitness expert who has helped &nbsp;&nbsp;hundreds of people just like you reach their health and fitness goals.</p>
    <p>More importantly, we will train your way using a variety of training styles including weights, kettle bells, full body strength and cardio, boxing and martial arts training keeping you interested and looking forward to your training sessions.</p>
  </section>

  <aside class="trainer-card">
    <div class="trainer-tab">ABOUT TRAINER</div>
    <h2 class="trainer-name">Daniel Hartley</h2>
    <ul class="credentials">
      <li><svg viewBox="0 0 18 18"><rect width="18" height="18" fill="#fff"/><path d="M4 9.5l3.2 3.2L14 5.5" fill="none" stroke="#2b8fd4" stroke-width="2.4"/></svg>Passion For the Fitness Industry for over 9 years</li>
      <li><svg viewBox="0 0 18 18"><rect width="18" height="18" fill="#fff"/><path d="M4 9.5l3.2 3.2L14 5.5" fill="none" stroke="#2b8fd4" stroke-width="2.4"/></svg>6 years Taekwondo 2nd degree Black Belt</li>
      <li><svg viewBox="0 0 18 18"><rect width="18" height="18" fill="#fff"/><path d="M4 9.5l3.2 3.2L14 5.5" fill="none" stroke="#2b8fd4" stroke-width="2.4"/></svg>3 Years Qualified Personal Trainer</li>
      <li><svg viewBox="0 0 18 18"><rect width="18" height="18" fill="#fff"/><path d="M4 9.5l3.2 3.2L14 5.5" fill="none" stroke="#2b8fd4" stroke-width="2.4"/></svg>2 year Boot Camp Instructor</li>
      <li><svg viewBox="0 0 18 18"><rect width="18" height="18" fill="#fff"/><path d="M4 9.5l3.2 3.2L14 5.5" fill="none" stroke="#2b8fd4" stroke-width="2.4"/></svg>Studied Kick Boxing, Muay Thai Boxing, Brazilian Jiu Jitsu Martial Arts (totalling over 4 years)</li>
      <li><svg viewBox="0 0 18 18"><rect width="18" height="18" fill="#fff"/><path d="M4 9.5l3.2 3.2L14 5.5" fill="none" stroke="#2b8fd4" stroke-width="2.4"/></svg>Qualified Advanced Sports Nutrition Course</li>
    </ul>
  </aside>

  <div class="gallery gallery-kettlebell" role="img" aria-label="Man training with kettlebells"></div>
  <div class="gallery gallery-boxing" role="img" aria-label="Woman in red boxing gloves"></div>
  <div class="gallery gallery-weights" role="img" aria-label="Arm lifting a dumbbell"></div>

  <p class="offer">Take Advantage of a Complimentary One on One Personal Training Session now by simply<br>contacting Daniel Hartley and organizing a convenient time</p>

  <footer class="contact-band">
    <div class="contact-label">For General &amp; Booking<br>Enquires Contact :</div>
    <span class="contact-divider" style="left:198px"></span>
    <div class="contact-person">DANIEL<br>HARTLEY</div>
    <span class="contact-divider" style="left:357px"></span>
    <div class="contact-phone">Call Now : 0491 570 156</div>
    <div class="contact-web">www.steadypulsewellness.com.au</div>
  </footer>
</main>
</body>
</html>
```